Building and Facilities Management brochure

Please refer to attached PDF, page by page with information about the brief.
SOPHISTICATED, BOLD, PROFESSIONAL BROCHURE to market our company in business meetings to Builders, Owners of buildings, Strata Committees etc.

The final design should portray quality, service, integrity,
Clear Communication

Attached is:
- pdf with details of basic layout options and wording and most of the information about the brief.
- Logo options to use
- Business card designs to understand what design we have previously had.
- Word document of the pdf if that helps to copy the information.

Target Market(s)

Professionals. Builders/developer, Strata Owners, and Building owners who want a high level of service and management of their building

Industry/Entity Type

It Company

Requirements
Must have
• - Logo
• - Contact details
• - Use of the colour in the design which has been specified.
• - Images/s of building/s
• - Use the phrase "Quality Service with Integrity"
Nice to have
• - as much of the wording as possible from the document which was uploaded, that will fit and work with the design
Should not have
• Excessive colour or variances as it needs to stay clear, bold and sophisticated.
• Too much on the page, clarity is key for clear communication without trying to clutter too much on the page.

```html
<!DOCTYPE html>
<html lang="en">
<head>
<meta charset="utf-8">
<title>Building and Facilities Management Brochure – Inside Spread</title>
<link href="https://fonts.googleapis.com/css2?family=Raleway:wght@300;400&family=Roboto:wght@400;700&display=swap" rel="stylesheet">
<style>
  :root {
    --page-bg: #8a8b8b;
    --brand-blue: #1f8fd6;
    --brand-blue-deep: #0f5f9e;
    --brand-blue-light: #3aa6e6;
    --photo-dark: #1d2a3a;
    --photo-mid: #6c7a8a;
    --photo-light: #d9dee3;
    --text-light: #ffffff;
  }
  * { box-sizing: border-box; margin: 0; padding: 0; }
  html, body {
    width: 1200px; height: 1200px; overflow: hidden;
    background: var(--page-bg);
  }
  .spread {
    position: absolute; left: 36px; top: 135px;
    width: 1128px; height: 930px;
    display: flex;
    box-shadow: 0 20px 40px rgba(0,0,0,0.25);
  }
  .panel { position: relative; height: 100%; overflow: hidden; }
  .panel-vision { width: 406px; }
  .panel-feature { width: 474px; }
  .panel-services { width: 248px; }

  .photo { position: absolute; inset: 0; }
  .photo-blue-left {
    background:
      linear-gradient(180deg, rgba(58,166,230,0.0) 0%, rgba(15,95,158,0.55) 100%),
      linear-gradient(100deg, var(--brand-blue-light) 0%, var(--brand-blue) 40%, var(--brand-blue-deep) 100%);
  }
  .photo-building {
    background:
      linear-gradient(180deg, var(--photo-light) 0%, var(--photo-mid) 35%, var(--photo-dark) 70%, var(--photo-mid) 90%, var(--photo-light) 100%);
  }
  .photo-blue-right {
    background: linear-gradient(180deg, var(--brand-blue-deep) 0%, var(--brand-blue) 55%, var(--brand-blue-deep) 100%);
  }

  .content { position: relative; color: var(--text-light); font-family: "Roboto", sans-serif; }
  .panel-heading {
    font-family: "Raleway", sans-serif; font-weight: 300;
    font-variant: small-caps; letter-spacing: 0.5px;
    line-height: 1; color: var(--text-light);
  }
  .vision-block { position: absolute; left: 36px; top: 36px; width: 320px; }
  .vision-block .panel-heading { font-size: 46px; margin-bottom: 12px; }
  .body-copy { font-size: 12.5px; line-height: 17px; }

  .aspects-block { position: absolute; left: 34px; top: 556px; width: 330px; }
  .aspects-block .panel-heading { font-size: 46px; margin-bottom: 10px; }
  .aspect-list { list-style: none; font-size: 12.5px; line-height: 17px; }
  .aspect-list strong { font-weight: 700; }

  .services-block { position: absolute; left: 32px; top: 48px; width: 200px; }
  .services-block .panel-heading { font-size: 44px; font-variant: normal; text-transform: uppercase; margin-bottom: 16px; }
  .services-copy { font-size: 12px; line-height: 17px; }
  .services-copy h3 { font-size: 12px; font-weight: 700; }
  .services-copy ul { list-style: none; }
  .services-copy li::before { content: "• "; }
</style>
</head>
<body>
  <main class="spread">
    <section class="panel panel-vision">
      <div class="photo photo-blue-left" role="img" aria-label="Blue-tinted photograph of modern apartment towers with balconies and a tree"></div>
      <div class="content">
        <div class="vision-block">
          <h2 class="panel-heading">Vision</h2>
          <p class="body-copy">At KVR, our aim is to provide complete solutions for Building and Facilities Owners and Strata Corporations in the management of their assets. With the understanding that each property has different needs and requirements, our focus is to work with clients to tailor solutions best suited to their specific needs.</p>
          <p class="body-copy">Our aim is to ensure the Building and Facilities are managed to the highest standards using the latest technological management solutions to efficiently and effectively control all aspects of the building. With a keen focus on controlling costs to ensure funds are spent costeffectively, through improved operations and management of all aspects of the building.</p>
        </div>
        <div class="aspects-block">
          <h2 class="panel-heading">Key Aspects</h2>
          <ul class="aspect-list">
            <li><strong>Compliance</strong> – with relevant industry acts and regulations</li>
            <li><strong>OH&amp;S</strong> – to ensure the building and aspects are controlled safely and the risk of all contractors and owners is reduced and managed.</li>
            <li><strong>Preventative Maintenance</strong> – to ensure assets are professionally maintained to ensure the best reliability and longevity of each asset.</li>
            <li><strong>Reactive Maintenance</strong> – to ensure any issues that arise are resolved and handled as efficiently as possible.</li>
            <li><strong>Communication</strong> – to ensure the Committee and Owners have clear and concise information and knowledge of the aspects of their building and assets</li>
            <li><strong>Relationships</strong> – are a top priority as they are paramount for effective management with Owners, Residents, Developers and Strata Managers</li>
          </ul>
        </div>
      </div>
    </section>

    <section class="panel panel-feature">
      <div class="photo photo-building" role="img" aria-label="Photograph of a white modern apartment building with glass balconies, dark louvres and a street tree"></div>
    </section>

    <section class="panel panel-services">
      <div class="photo photo-blue-right" role="img" aria-label="Blue-tinted photograph of a high-rise apartment facade"></div>
      <div class="content">
        <div class="services-block">
          <h2 class="panel-heading">Services</h2>
          <div class="services-copy">
            <h3>Core Services</h3>
            <p>These are the core focus of the business to provide the highest standard in Building and Facilities Management.</p>
            <ul>
              <li>Building Management</li>
              <li>Facilities Management</li>
              <li>Caretaker</li>
            </ul>
            <h3>Value Added Services</h3>
            <p>In addition to the Core Service we are proud to offer these Value-Added services to complement the management of the Building, or offer as stand-alone services to assist owners with the management of their Building and Assets.</p>
            <ul>
              <li>Concierge</li>
              <li>Cleaning</li>
              <li>Project Management</li>
              <li>Electrical</li>
              <li>Handyman</li>
              <li>New site setup</li>
              <li>Building defect management</li>
            </ul>
            <p>Please feel free to contact us to enquire about any of the above services, either individually or as multiple services to ensure the best value can be provided for your requirements.</p>
          </div>
        </div>
      </div>
    </section>
  </main>
</body>
</html>
```